eBook Lumio

I currently use the free eBook app Lumio avail from tolvex

I would like an app to be developed the same but with the following options

But I would like an option in my book listing to mark off the books I've already read.

Maybe also an option to rate the book as well.

Option to choose different bookshelves
Like a nice white beachy looking one
Dark timber very formal
Colourful funky

Target Market(s)

All readers who love to carry all there books with them

Requirements
Must have
• Similar bookshelf look
Either be able to list books or show thumbnail of books
Epub and PDF format
Able to sort by Titles, Author or Catergories
Must have a search field
Nice to have
• Option to choose different bookshelves
Dark timber very formal
Colourful funky

```html
<!DOCTYPE html>
<html lang="en">
<head>
<meta charset="utf-8">
<title>eBook Lumio</title>
<link href="https://fonts.googleapis.com/css2?family=Arimo:wght@400;700&display=swap" rel="stylesheet">
<style>
  :root {
    --bg-light: #f6f6f6;
    --bg-dark: #d6d6d6;
    --ink: #111111;
    --status: #0c0c0c;
    --wood-light: #d9a35c;
    --wood-mid: #b8752f;
    --wood-dark: #8a4f1c;
    --shelf-edge: #e6b86e;
    --bar-top: #d7a869;
    --bar-bottom: #a9702f;
    --bar-text: #4a2a0c;
    --tab-bg: #c89452;
    --tab-active: #e9cf9f;
    --paper: #f6ecdc;
    --rule: #7a6a5a;
    --cover-band: #1f8a8f;
    --page: #ffffff;
  }
  * { box-sizing: border-box; margin: 0; padding: 0; }
  html, body { width: 1200px; height: 900px; overflow: hidden; }
  body {
    font-family: "Arimo", Arial, sans-serif;
    background: radial-gradient(ellipse at 50% 40%, var(--bg-light) 0%, var(--bg-dark) 100%);
    position: relative;
    color: var(--ink);
  }
  .headline {
    position: absolute; top: 48px; left: 0; width: 1200px;
    text-align: center; font-size: 64px; font-weight: 700;
    letter-spacing: 1px;
    text-shadow: 0 2px 3px rgba(0,0,0,.35);
  }
  .screen {
    position: absolute; overflow: hidden;
    background: linear-gradient(90deg, var(--wood-mid), var(--wood-light) 50%, var(--wood-mid));
    box-shadow: 0 8px 24px rgba(0,0,0,.35);
  }
  .screen--list { left: 72px; top: 252px; width: 320px; height: 452px; }
  .screen--shelf { left: 410px; top: 218px; width: 382px; height: 506px; z-index: 2; }
  .screen--page { left: 810px; top: 252px; width: 318px; height: 452px; }

  .status {
    height: 12px; background: var(--status); color: #fff;
    font-size: 7px; display: flex; justify-content: space-between;
    align-items: center; padding: 0 6px;
  }
  .status__time { position: absolute; left: 0; right: 0; text-align: center; }
  .toolbar {
    height: 18px; display: flex; align-items: center; justify-content: space-between;
    padding: 0 6px; position: relative;
    background: linear-gradient(var(--bar-top), var(--bar-bottom));
    border-bottom: 1px solid var(--wood-dark);
  }
  .toolbar__title {
    position: absolute; left: 0; right: 0; text-align: center;
    font-size: 10px; font-weight: 700; color: var(--bar-text); pointer-events: none;
  }
  .btn {
    font-size: 6px; font-weight: 700; color: #fff; padding: 2px 6px;
    border-radius: 3px; background: linear-gradient(#b77a36, #7d4818);
    border: 1px solid #5e3610; position: relative;
  }
  .toolbar__tools { display: flex; gap: 5px; align-items: center; position: relative; }
  .tabs {
    height: 16px; display: flex; align-items: center; gap: 4px; padding: 0 4px;
    background: linear-gradient(var(--bar-top), var(--bar-bottom));
  }
  .tabs__arrow { width: 0; height: 0; border-top: 5px solid transparent; border-bottom: 5px solid transparent; }
  .tabs__arrow--left { border-right: 7px solid #6e3d12; }
  .tabs__arrow--right { border-left: 7px solid #6e3d12; }
  .tabs__group {
    display: flex; border: 1px solid #6e3d12; border-radius: 3px; overflow: hidden;
    background: var(--tab-bg);
  }
  .tab { font-size: 6px; font-weight: 700; color: var(--bar-text); padding: 2px 6px; }
  .tab--active { background: var(--tab-active); }
  .search {
    flex: 1; height: 10px; border-radius: 5px; background: var(--tab-active);
    border: 1px solid #6e3d12; position: relative;
  }
  .search svg { position: absolute; right: 3px; top: 1px; }

  .shelves { position: relative; height: 460px; }
  .shelf {
    position: absolute; left: 0; right: 0; height: 7px;
    background: linear-gradient(var(--shelf-edge), var(--wood-mid));
    box-shadow: 0 4px 6px rgba(0,0,0,.35);
  }
  .book-thumb {
    position: absolute; left: 18px; top: 19px; width: 50px; height: 68px;
    box-shadow: 2px 2px 4px rgba(0,0,0,.4); background: #fff;
  }
  .book-thumb__art { height: 56px; background: linear-gradient(#d8d8d8, #8a8a8a); }
  .book-thumb__band {
    height: 12px; background: var(--cover-band); color: #fff;
    font-size: 8px; font-weight: 700; text-align: center; line-height: 12px;
  }

  .list {
    position: absolute; left: 8px; right: 0; top: 46px; bottom: 8px;
    background: repeating-linear-gradient(var(--paper) 0 19px, var(--rule) 19px 20px);
  }
  .list__row { display: flex; gap: 6px; padding: 4px 3px; height: 20px; }
  .list__icon { width: 13px; height: 13px; background: linear-gradient(#ccc, #777); border-bottom: 3px solid var(--cover-band); }
  .list__title { font-size: 8px; font-weight: 700; line-height: 8px; }
  .list__sub { font-size: 5px; color: #555; }

  .page {
    position: absolute; left: 0; right: 14px; top: 18px; bottom: 8px;
    background: var(--page); box-shadow: 3px 0 0 #e8e8e8, 6px 0 0 #d4d4d4;
    text-align: center;
  }
  .page__art {
    margin: 24px auto 0; width: 250px; height: 250px;
    background: radial-gradient(circle, #555 0%, #222 55%, #fff 72%);
  }
  .page__title { font-size: 40px; font-weight: 700; margin-top: 12px; line-height: 1; }
  .page__sub { font-size: 20px; color: #333; }
</style>
</head>
<body>
  <h1 class="headline">eBook Lumio</h1>

  <section class="screen screen--list" aria-label="Book list view">
    <div class="status"><span>Slate</span><span class="status__time">8:02</span><span></span></div>
    <div class="toolbar"><span class="btn">Store</span><span class="toolbar__title">eBook Lumio</span><span></span></div>
    <div class="tabs">
      <span class="tabs__arrow tabs__arrow--left"></span>
      <div class="tabs__group">
        <span class="tab tab--active">All</span><span class="tab">Books</span><span class="tab">PDFs</span>
        <span class="tab">Recent</span><span class="tab">Favourite</span><span class="tab">Crime</span><span class="tab">Romance</span>
      </div>
      <span class="tabs__arrow tabs__arrow--right"></span>
    </div>
    <div class="list">
      <div class="list__row">
        <div class="list__icon" role="img" aria-label="Small cover of Paradise"></div>
        <div><p class="list__title">PARADISE</p><p class="list__sub">Paradise</p></div>
      </div>
    </div>
  </section>

  <section class="screen screen--shelf" aria-label="Bookshelf view">
    <div class="status"><span>Slate</span><span class="status__time">8:02</span><span>45%</span></div>
    <div class="toolbar">
      <span class="btn">Store</span>
      <span class="toolbar__title">eBook Lumio</span>
      <span class="toolbar__tools">
        <svg width="22" height="11" viewBox="0 0 22 11" aria-hidden="true">
          <rect x="0" y="0" width="22" height="11" rx="2" fill="#7d4818"/>
          <rect x="2" y="2" width="3" height="3" fill="#fff"/><rect x="6" y="2" width="3" height="3" fill="#fff"/>
          <rect x="2" y="6" width="3" height="3" fill="#fff"/><rect x="6" y="6" width="3" height="3" fill="#fff"/>
          <rect x="12" y="2" width="8" height="1.5" fill="#fff"/><rect x="12" y="4.8" width="8" height="1.5" fill="#fff"/>
          <rect x="12" y="7.6" width="8" height="1.5" fill="#fff"/>
        </svg>
        <span class="btn">Edit</span>
      </span>
    </div>
    <div class="tabs">
      <span class="tabs__arrow tabs__arrow--left"></span>
      <div class="tabs__group">
        <span class="tab tab--active">All</span><span class="tab">Books</span><span class="tab">PDFs</span>
        <span class="tab">Recent</span><span class="tab">Favourite</span><span class="tab">Crime</span><span class="tab">Romance</span>
      </div>
      <span class="tabs__arrow tabs__arrow--right"></span>
      <div class="search">
        <svg width="8" height="8" viewBox="0 0 8 8" aria-hidden="true"><circle cx="3" cy="3" r="2.2" fill="none" stroke="#6e3d12" stroke-width="1"/><line x1="4.6" y1="4.6" x2="7.5" y2="7.5" stroke="#6e3d12" stroke-width="1.2"/></svg>
      </div>
    </div>
    <div class="shelves">
      <div class="book-thumb">
        <div class="book-thumb__art" role="img" aria-label="Ornamental cover art of Paradise"></div>
        <div class="book-thumb__band">PARADISE</div>
      </div>
      <div class="shelf" style="top:88px"></div>
      <div class="shelf" style="top:182px"></div>
      <div class="shelf" style="top:274px"></div>
      <div class="shelf" style="top:366px"></div>
      <div class="shelf" style="top:456px"></div>
    </div>
  </section>

  <section class="screen screen--page" aria-label="Reading view">
    <div class="status"><span></span><span class="status__time">8:02</span><span>45%</span></div>
    <article class="page">
      <div class="page__art" role="img" aria-label="Large ornamental flourished letter P cover illustration"></div>
      <p class="page__title">Paradise</p>
      <p class="page__sub">Paradise</p>
    </article>
  </section>
</body>
</html>
```